lotus bowl vietnamese restaurant in need of a new menu

a family owned vietnamese restaurant in need of a new menu design that is fun, classy, and yet simple. menu that will catch the customers eyes. easy to read yet flows nicely. like to use the color green (basil green color) creme yellow and maroon. open to other colors as long as it looks nice together. our restaurant is family oriented, casual yet has a nice ambiance atmosphere.
prefer 11x17 portrait double sided. attached is our menu with the current price updated so use the info on this to start creating! looking for something unique, professional and one of a kind menu!
please use your own creative layout and design. we are open to ideas. the files uploaded are the updated prices and the logo is to use whichever one you feel goes with the menu.
Reason: don't see anything we like so far...please be creative!
Target Market(s)
restaurant consumers
Industry/Entity Type
Restaurant
Look and feel

```html
<!DOCTYPE html>
<html lang="en">
<head>
<meta charset="utf-8">
<title>Lotus Bowl – Take Out Menu (Front)</title>
<link href="https://fonts.googleapis.com/css2?family=Roboto+Condensed:wght@400;700&family=PT+Sans:wght@700&family=Oswald:wght@400&display=swap" rel="stylesheet">
<style>
  :root{
    --lime-bg:#c9f25c;
    --basil:#43d81f;
    --basil-border:#7fe02c;
    --cream:#fdfbda;
    --maroon:#c4121a;
    --ink:#1d1d1b;
    --flame:#f07a1a;
  }
  html,body{margin:0;padding:0;width:1200px;height:1200px;overflow:hidden;background:var(--lime-bg);}
  .stage{position:relative;width:1500px;height:1500px;transform:scale(.8);transform-origin:0 0;
    font-family:"Roboto Condensed",Arial Narrow,sans-serif;color:var(--ink);}
  .side-label{position:absolute;left:48px;top:84px;font-family:"Roboto Condensed",sans-serif;font-weight:400;font-size:66px;color:#22dd22;letter-spacing:1px;}
  .menu-card{position:absolute;left:275px;top:15px;width:934px;height:1454px;background:var(--cream);
    border:8px solid var(--basil-border);box-shadow:6px 6px 10px rgba(0,0,0,.35);}
  .abs{position:absolute;}
  .takeout-band{left:302px;top:60px;width:248px;height:40px;background:var(--maroon);color:#fff;
    font-family:"Oswald",sans-serif;font-size:31px;line-height:40px;text-align:center;letter-spacing:1px;}
  .brand-name{left:600px;top:34px;width:300px;text-align:center;font-family:"PT Sans",sans-serif;font-weight:700;
    font-size:54px;line-height:46px;color:var(--basil);}
  .brand-mark{left:735px;top:140px;width:30px;height:30px;border-radius:50%;background:var(--basil);}
  .tagline{left:590px;top:210px;width:320px;text-align:center;font-weight:700;font-size:33px;color:var(--basil);
    white-space:nowrap;line-height:36px;}
  .tagline-rule{left:596px;top:246px;width:308px;height:2px;background:var(--basil);}
  .contact{left:585px;top:251px;width:330px;text-align:center;font-size:11.5px;white-space:nowrap;line-height:14px;}
  .hero-photo{left:910px;top:22px;width:310px;height:292px;border-radius:0 0 0 60%;
    background:radial-gradient(circle at 60% 40%,#c9e79a 0%,#7fb548 45%,#4f8a2b 70%,#d4311f 72%,#b8261a 100%);}
  .thumb{border:3px solid var(--basil-border);border-radius:7px;background:linear-gradient(135deg,#f1c58a,#c8693a 55%,#7d8f3d);}
  .thumb.soft{background:linear-gradient(135deg,#f3e2c2,#d9a25a 60%,#9bb56a);}
  .thumb.green{background:linear-gradient(135deg,#b9d98e,#6e9b48 50%,#d9b37c);}
  .thumb.grill{background:linear-gradient(135deg,#6b3a22,#a55a30 50%,#3c5a26);}
  .divider{left:749px;top:292px;width:2px;height:1156px;background:var(--maroon);}
  .divider-tip{width:10px;height:10px;background:var(--maroon);transform:rotate(45deg);left:745px;}
  .section-title{font-family:"PT Sans",sans-serif;font-weight:700;font-size:22px;color:var(--maroon);}
  .section-note{font-size:13.5px;color:var(--maroon);line-height:15px;}
  .intro{font-size:13.5px;line-height:15px;font-style:italic;}
  .item{font-size:14px;line-height:15px;}
  .item b{font-weight:700;font-size:14.5px;}
  .item.large b{font-size:17px;}
  .col-left{left:300px;}
  .col-right{left:770px;}
  .flame{width:14px;height:16px;vertical-align:-2px;margin-left:8px;}
  .extras{left:770px;top:1392px;width:430px;height:66px;background:var(--basil);border-radius:4px;color:#fff;
    font-size:8.5px;line-height:10px;}
  .extras div{position:absolute;top:8px;}
</style>
</head>
<body>
<div class="stage">
  <div class="side-label">FRONT</div>
  <div class="menu-card"></div>

  <div class="abs takeout-band">TAKE OUT MENU</div>
  <div class="abs brand-name">LOTUS<br>BOWL</div>
  <div class="abs brand-mark"></div>
  <div class="abs tagline">Vietnamese Restaurant</div>
  <div class="abs tagline-rule"></div>
  <div class="abs contact">(954) 555-0182 &nbsp;|&nbsp; 2150 Palm Grove Ave &nbsp;|&nbsp; Coral Ridge, FL 33000</div>
  <div class="abs hero-photo" role="img" aria-label="Bowl of pho with herbs, lime, jalapeño and noodles"></div>

  <div class="abs divider"></div>
  <div class="abs divider-tip" style="top:292px"></div>
  <div class="abs divider-tip" style="top:1438px"></div>

  <!-- Left column -->
  <div class="abs section-title col-left" style="top:124px">Appetizers</div>
  <div class="abs intro col-left" style="top:152px;width:220px;font-size:11px;line-height:12.5px"><b>Spring Rolls (2)</b> comes with lettuce, vermicelli noodles rolled in rice paper served with peanut sauce with choice of: (cannot be mixed):</div>

  <div class="abs item col-left" style="top:200px"><b>1. Goi Cuon Tom &amp; Thit Heo | 4.50</b><br>Shrimp &amp; pork spring rolls</div>
  <div class="abs item col-left" style="top:245px;width:300px"><b>2. Goi Cuon Thit Heo / Ga / or Bo Nuong | 5.50</b><br>Choice of: grilled pork / grilled chicken or<br>grilled beef spring rolls</div>
  <div class="abs item col-left" style="top:304px"><b>3. Bi Cuon | 4.50</b><br>Pork skin roasted with rice powder spring rolls</div>
  <div class="abs item col-left" style="top:349px"><b>4. Cha Gio (2) | 4.50</b><br>Fried eggrolls with shrimp, pork &amp; Vegetables rolled in egg wrap</div>
  <div class="abs item col-left" style="top:393px"><b>5. Canh Ga Nuoc Mam (6) | 7.95</b><br>Fried chicken wings</div>
  <div class="abs item col-left" style="top:438px"><b>6. Gio Tom (4)| 5.95</b><br>Fried shrimp rolls</div>
  <div class="abs item col-left" style="top:482px"><b>7. Ca Vien Chien (8) | 4.95</b><br>Fried fish balls</div>
  <div class="abs item col-left" style="top:527px"><b>8. Chao Tom (2) | 7.95</b><br>Grilled shrimp paste wrapped<br>around sugar cane stick</div>
  <div class="abs item col-left" style="top:586px"><b>9. Wonton Soup (s) | 4.95 (L) 7.50</b><br>Wonton shrimp &amp; pork soup</div>
  <div class="abs item col-left" style="top:631px"><b>10. Tom Cua Soup (S) | 4.95 (L) 7.50</b><br>Crab meat, shrimp &amp; egg soup</div>
  <div class="abs item col-left" style="top:675px"><b>Vietnamese Salad</b> comes with thin cabbage,<br>carrots, onions, mints, crushed peanuts tossed<br>in lime juice &amp; vinegar with the following choices of:</div>
  <div class="abs item col-left" style="top:734px"><b>11. Goi Ga - Chicken Salad | 8.95</b></div>
  <div class="abs item col-left" style="top:764px"><b>12. Goi Tom - Shrimp Salad | 9.95</b></div>
  <div class="abs item col-left" style="top:793px"><b>13. Bo Tai Chanh |11.95</b><br>Rare thin sliced beef with onions, mints, basils,<br>Crushed peanuts in lime juice &amp; vinegar</div>
  <div class="abs item col-left" style="top:853px"><b>14. Chim Cut Roti | 11.95</b><br>Roasted quails served with salt &amp; pepper</div>

  <div class="abs section-title col-left" style="top:903px">Hu Tieu (Mi) - Noodle Soup</div>
  <div class="abs section-note col-left" style="top:929px">Pork Broth With Rice Or Egg Noodle</div>
  <div class="abs item col-left" style="top:958px"><b>15. Hu Tieu / Mi Dac Biet | 10.50</b><br>Choice of: rice or egg noodle with shrimp, roast pork,<br>chicken, imitation crab, quail eggs, ground pork &amp; fried<br>shrimp cracker combination noodle soup</div>
  <div class="abs item col-left" style="top:1034px"><b>16. Hu Tieu / Mi Hai San | 11.50</b><br>Choice of: rice or egg noodle with shrimp, scallop,<br>squid, fish balls &amp; imitation crab noodle soup</div>
  <div class="abs item col-left" style="top:1095px"><b>17. Hu Tieu Mytho | 9.95</b><br>Shrimp, roast pork, chicken, fish ball, imitation<br>crab &amp; ground pork with clear noodle soup</div>
  <div class="abs item col-left" style="top:1156px"><b>18. Hu Tieu Sate | 9.50</b><svg class="flame" viewBox="0 0 14 16"><path d="M7 0C8 4 12 6 12 10a5 5 0 0 1-10 0c0-3 2-4 2-6 1 1 1 3 2 3 1-2 1-4 1-7z" fill="var(--flame)"/></svg><br>Beef with tomato slices, cucumber, bean sprouts<br>&amp; crushed peanuts in spicy noodle soup</div>
  <div class="abs item col-left" style="top:1217px"><b>19. Hu Tieu / Mi Kho Dac Biet | 10.95</b><br>Choice of: rice or egg noodle with shrimp,<br>roast pork, chicken, imitation crab, ground pork<br>and fried shrimp cracker with soup on the side</div>
  <div class="abs item col-left" style="top:1293px"><b>20. Mi Hoanh Thanh | 8.95</b><br>Wonton with egg noodle soup</div>
  <div class="abs item col-left" style="top:1339px"><b>21. +XA XIU (ROAST PORK ) | 9.95</b></div>
  <div class="abs item col-left" style="top:1369px"><b>22. Banh Canh Tom Thit Gio Heo | 9.50</b><br>Shrimp, pork knuckle &amp; vietnamese big noodle soup</div>
  <div class="abs item col-left" style="top:1415px"><b>23. Banh Canh Ga | 8.95</b><br>Chicken with vietnamese big noodle soup</div>

  <!-- Left thumbnails -->
  <div class="abs thumb soft" style="left:625px;top:433px;width:102px;height:59px" role="img" aria-label="Fresh spring rolls with shrimp"></div>
  <div class="abs thumb" style="left:625px;top:511px;width:102px;height:59px" role="img" aria-label="Fried eggrolls"></div>
  <div class="abs thumb soft" style="left:625px;top:589px;width:102px;height:60px" role="img" aria-label="Wonton soup"></div>
  <div class="abs thumb" style="left:625px;top:1048px;width:102px;height:59px" role="img" aria-label="Fried shrimp rolls"></div>
  <div class="abs thumb green" style="left:625px;top:1126px;width:102px;height:59px" role="img" aria-label="Vietnamese salad"></div>
  <div class="abs thumb soft" style="left:625px;top:1203px;width:102px;height:59px" role="img" aria-label="Noodle soup with herbs"></div>
  <div class="abs thumb green" style="left:625px;top:1285px;width:102px;height:59px" role="img" aria-label="Wonton egg noodle soup"></div>

  <!-- Right column -->
  <div class="abs section-title col-right" style="top:298px">Pho - Rice Noodle Soup</div>
  <div class="abs item col-right" style="top:336px"><b>24. Pho Dac Biet | 9.50</b><br>Steak, brisket, flank, tendon, tripe &amp;<br>meatballs combination noodle soup</div>
  <div class="abs item col-right" style="top:397px"><b>25. Pho | 8.50</b><br>Noodle soup with choices up to 3 items:<br>steak, brisket, flank, tendon, tripe, meatball or vegetables</div>
  <div class="abs item col-right" style="top:457px"><b>26. Pho Ga Vietnam (Ga Di Bo) | 10.50</b><br>Free range chicken noodle soup</div>
  <div class="abs item col-right" style="top:503px"><b>27. Pho Ga My | 9.50</b><br>White chicken &amp; mixed vegetables noodle soup</div>
  <div class="abs item col-right" style="top:549px"><b>28. Pho Thit Heo / Bo / or Ga Nuong | 10.50</b><br>Choice of: grilled pork, grilled beef or grilled<br>chicken with mixed vegetables noodle soup</div>
  <div class="abs item col-right" style="top:610px"><b>29. Pho Do Bien | 11.50</b><br>Shrimp, scallop, squid, fish balls, imitation crab &amp;<br>vegetables seafood noodle soup</div>
  <div class="abs item col-right" style="top:671px"><b>30. Pho Tom | 9.75</b><br>Shrimp with mixed vegetables noodle soup</div>
  <div class="abs item col-right" style="top:716px"><b>31. Pho Do Bien Chua Cay | 11.50</b><svg class="flame" viewBox="0 0 14 16"><path d="M7 0C8 4 12 6 12 10a5 5 0 0 1-10 0c0-3 2-4 2-6 1 1 1 3 2 3 1-2 1-4 1-7z" fill="var(--flame)"/></svg><br>Shrimp, scallop, squid, fish balls &amp;<br>imitation crab in hot &amp; sour noodle soup</div>
  <div class="abs item col-right" style="top:777px"><b>32. Pho Tre Em | 7.25</b><br>Kid's steak &amp; meatball noodle soup</div>

  <div class="abs section-title col-right" style="top:822px">Bun - Vermicelli Noodle Bowl</div>
  <div class="abs section-note col-right" style="top:850px">All vermicelli bowl comes with fresh lettuce, bean sprouts,<br>sliced cucumbers, shredded carrots &amp; crushed peanuts</div>
  <div class="abs item large col-right" style="top:892px"><b>33. Bun Dac Biet | 12.95</b><br>Choice of: grilled pork, grilled chicken or<br>grilled beef with grilled shrimp &amp; fried<br>eggroll special combination vermicelli bowl</div>
  <div class="abs item large col-right" style="top:968px"><b>34. Bun - Vermicelli Bowl | 9.50</b><br>Choice of: grilled pork,<br>Grilled chicken or grilled beef<br>35. + eggroll | 9.95</div>
  <div class="abs item large col-right" style="top:1044px"><b>36. + Shrimp | 10.50</b></div>
  <div class="abs item large col-right" style="top:1078px"><b>37. Bun Tom Nuong (8) | 10.95</b><br>Grilled shrimp with<br>Vermicelli noodle bowl</div>
  <div class="abs item large col-right" style="top:1140px"><b>38. Bun Cha Gio (3) | 9.50</b><br>Fried eggroll vermicelli bowl</div>
  <div class="abs item large col-right" style="top:1186px"><b>39. Bun Chao Tom (2) | 9.50</b><br>Grilled shrimp paste vermicelli bowl</div>
  <div class="abs item large col-right" style="top:1232px"><b>* 40. Bun Bo Hue | 9.50</b><br>Spicy beef noodle soup with beef shank, pork knuckle,<br>pork blood with large vermicelli noodles</div>
  <div class="abs item large col-right" style="top:1294px"><b>* 41. Bun Rieu | 9.50</b><br>Mixed ground pork &amp; crab, pork blood, dried tofu with<br>vermicelli rice noodle in tomato broth soup</div>
  <div class="abs item large col-right" style="top:1356px"><b>* 42. Bun Mang Vit | 9.50</b><br>Duck &amp; bamboo vermicelli noodle soup</div>

  <!-- Right thumbnails -->
  <div class="abs thumb grill" style="left:1028px;top:686px;width:166px;height:116px" role="img" aria-label="Grilled pork vermicelli bowl with eggroll"></div>
  <div class="abs thumb green" style="left:1028px;top:894px;width:166px;height:100px" role="img" aria-label="Grilled shrimp over fresh greens"></div>
  <div class="abs thumb grill" style="left:1028px;top:1012px;width:166px;height:101px" role="img" aria-label="Bun bo hue, number 40"></div>
  <div class="abs thumb" style="left:1028px;top:1130px;width:166px;height:100px" role="img" aria-label="Bun rieu, number 41"></div>

  <div class="abs extras">
    <div style="left:32px">* X-large | 2.00 more<br>* Extra meat (steak, chicken, etc.) | 3.50<br>* Extra shrimp | 3.00<br>* Extra herbs or vegetables | 1.50<br>&nbsp;&nbsp;(Ex: onions, culantros, basils, beansprouts, etc.)</div>
    <div style="left:242px">* Extra rice, soup or noodles | 1.50<br>* Change noodle or brown rice | 2.00<br>* Add fried egg | 1.50<br>* Add or change to fried rice | 3.00<br>* Add eggroll | 2.25</div>
  </div>
</div>
</body>
</html>
```